Business Card design for a skin clinic

i would like a business card design for our skin clinic.
our logo colors are Blue and Grey and Bule /white.
we are searching for a minimalistic design yet very elegant,dynamic and professional which can reflect a professional medical skin care clinic( not a beauty salon).
THE DESGIN IS NOT FOR A PERSON IT WILL BE USED IN THE CLINIC FOR CLIENTS SO THERE SHOULD BE NO NAME OF A PERSON ONLY THE CLINIC NAME AND THE CONTACT INFO

Target Market(s)
young and old womens
Industry/Entity Type
Business
Contact Information for Business Card
we have 2 address and both should be on the card.
address A: Lindenhoflaan 214B, 3041KP Rotterdam, Tel 010 483 21 95
address B: Zonnewijzerstraat 238, 1062RT Amsterdam Tel 020 571 3829
website www.huidpuntzorg.nu, email info@huidpuntzorg.nu
Look and feel
Each slider illustrates characteristics of the customer's brand and the style your logo design should communicate.

```html
<!DOCTYPE html>
<html lang="nl">
<head>
<meta charset="utf-8">
<title>Huidpuntzorg – Business Card</title>
<link rel="stylesheet" href="https://fonts.googleapis.com/css2?family=Questrial&family=Lato:wght@400;700&family=Montserrat:wght@600&display=swap">
<style>
  :root {
    --backdrop: #d6d6d6;
    --card: #ffffff;
    --blue-1: #1f5fa8;
    --blue-2: #2b86cc;
    --blue-3: #2a9ad8;
    --blue-4: #3aaee0;
    --blue-5: #1e72bd;
    --blue-6: #1a5ba6;
    --brand-blue: #2a8fd4;
    --ink: #1c1c1c;
    --grey: #7a7a7a;
    --strip-light: #e6e6e6;
    --strip-dark: #c4c4c4;
  }
  * { margin: 0; padding: 0; box-sizing: border-box; }
  html, body {
    width: 1200px; height: 800px; overflow: hidden;
    background: var(--backdrop);
  }
  .stage { position: relative; width: 1200px; height: 800px; }

  .card {
    position: absolute; top: 272px;
    width: 472px; height: 262px;
    background: var(--card);
    overflow: hidden;
  }
  .card--front { left: 61px; }
  .card--back { left: 641px; }

  .band {
    position: absolute; left: 0; width: 100%; height: 29px;
    display: flex;
  }
  .band span { flex: 1; }
  .band--top { top: 0; }
  .band--top span:nth-child(1) { background: var(--blue-1); }
  .band--top span:nth-child(2) { background: var(--blue-2); }
  .band--top span:nth-child(3) { background: var(--blue-3); }
  .band--top span:nth-child(4) { background: var(--blue-4); }
  .band--bottom { bottom: 0; }
  .band--bottom span:nth-child(1) { background: var(--blue-4); }
  .band--bottom span:nth-child(2) { background: var(--blue-3); }
  .band--bottom span:nth-child(3) { background: var(--blue-5); }
  .band--bottom span:nth-child(4) { background: var(--blue-6); }

  .brand {
    position: absolute; text-align: center;
    font-family: "Questrial", sans-serif;
  }
  .brand__dot {
    display: block; margin: 0 auto;
    border-radius: 50%;
    background: var(--brand-blue);
  }
  .brand__name {
    display: block; color: var(--brand-blue);
    font-family: "Montserrat", sans-serif; font-weight: 600;
    letter-spacing: 0.06em; white-space: nowrap;
  }
  .brand__tagline {
    display: block; color: var(--grey);
    letter-spacing: 0.08em; white-space: nowrap;
  }

  .card--front .brand { left: 0; width: 100%; top: 62px; }
  .card--front .brand__dot { width: 46px; height: 46px; margin-bottom: 18px; }
  .card--front .brand__name { font-size: 30px; line-height: 36px; }
  .card--front .brand__tagline { font-size: 13px; margin-top: 6px; }

  .card--back .brand { left: 0; width: 221px; top: 86px; }
  .card--back .brand__dot { width: 32px; height: 32px; margin-bottom: 16px; }
  .card--back .brand__name { font-size: 21px; line-height: 26px; }
  .card--back .brand__tagline { font-size: 10px; margin-top: 4px; }

  .divider-strip {
    position: absolute; left: 221px; top: 0;
    width: 32px; height: 100%;
    background: linear-gradient(160deg, var(--strip-light), var(--strip-dark) 50%, var(--strip-light));
  }
  .icon-column {
    position: absolute; left: 222px; top: 62px;
    width: 31px; list-style: none;
  }
  .icon-column li {
    height: 38px; display: flex; align-items: center; justify-content: center;
  }
  .icon-column li:nth-child(1) { background: var(--blue-4); }
  .icon-column li:nth-child(2) { background: var(--blue-3); }
  .icon-column li:nth-child(3) { background: var(--blue-5); }
  .icon-column li:nth-child(4) { background: var(--blue-6); }
  .icon-column svg { width: 14px; height: 14px; fill: #fff; }

  .contact {
    position: absolute; left: 284px; top: 50px; width: 176px;
    font-family: "Lato", sans-serif; color: var(--ink);
  }
  .contact__heading {
    font-family: "Montserrat", sans-serif; font-weight: 600;
    font-size: 15px; line-height: 18px; letter-spacing: 0.02em;
  }
  .contact__sub {
    color: var(--brand-blue); font-size: 12px; line-height: 15px;
    margin-bottom: 6px;
  }
  .contact__group { font-size: 12px; line-height: 14px; white-space: nowrap; }
  .contact__group--address { font-size: 11.5px; line-height: 13.5px; }
  .contact__group--address p + p.address-start { margin-top: 3px; }
  .contact__rule {
    width: 44px; height: 2px; background: var(--blue-5);
    margin: 4px 0 5px;
  }
</style>
</head>
<body>
<main class="stage">
  <section class="card card--front" aria-label="Card front">
    <div class="band band--top"><span></span><span></span><span></span><span></span></div>
    <div class="brand">
      <span class="brand__dot"></span>
      <span class="brand__name">HUIDPUNTZORG</span>
      <span class="brand__tagline">next generation skin care</span>
    </div>
    <div class="band band--bottom"><span></span><span></span><span></span><span></span></div>
  </section>

  <section class="card card--back" aria-label="Card back">
    <div class="brand">
      <span class="brand__dot"></span>
      <span class="brand__name">HUIDPUNTZORG</span>
      <span class="brand__tagline">next generation skin care</span>
    </div>

    <div class="divider-strip"></div>
    <ul class="icon-column">
      <li><svg viewBox="0 0 16 16"><circle cx="8" cy="4.5" r="3.2"/><path d="M2 15c0-3.6 2.7-6 6-6s6 2.4 6 6z"/></svg></li>
      <li><svg viewBox="0 0 16 16"><path d="M3.6 1.2l2.3 2.9-1.3 1.6c.9 2 2.5 3.7 4.5 4.6l1.6-1.3 2.9 2.3-1.5 2.5C6.9 13.5 2.5 9.1 1.2 3z"/></svg></li>
      <li><svg viewBox="0 0 16 16"><circle cx="8" cy="8" r="7"/><path d="M4 5c1.5-.5 2.5.5 2 2-.4 1.2 1 1.6 1.2 3 .1 1-.6 2-.6 3M10 2.5c0 1.5 1.5 1.5 2 3s2 1.5 2.3 2.3" stroke="#1e72bd" stroke-width="1.3" fill="none"/></svg></li>
      <li><svg viewBox="0 0 16 16"><path d="M8 .8a5 5 0 0 0-5 5c0 3.8 5 9.4 5 9.4s5-5.6 5-9.4a5 5 0 0 0-5-5zm0 7a2 2 0 1 1 0-4 2 2 0 0 1 0 4z"/></svg></li>
    </ul>

    <div class="contact">
      <p class="contact__heading">SKIN CLINIC</p>
      <p class="contact__sub">Rotterdam · Amsterdam</p>
      <div class="contact__group">
        <p>010 483 21 95</p>
        <p>020 571 3829</p>
      </div>
      <div class="contact__rule"></div>
      <div class="contact__group">
        <p>info@huidpuntzorg.nu</p>
        <p>www.huidpuntzorg.nu</p>
      </div>
      <div class="contact__rule"></div>
      <div class="contact__group contact__group--address">
        <p>Lindenhoflaan 214B</p>
        <p>3041KP Rotterdam</p>
        <p class="address-start">Zonnewijzerstraat 238</p>
        <p>1062RT Amsterdam</p>
      </div>
    </div>
  </section>
</main>
</body>
</html>
```